"Hollow Lanterns" Women's Fiction Book Cover

The title of the book is "Hollow Lanterns," and the author name is M.J. Lowe. It's women's fiction, but with a subtle supernatural flair. I'm just looking for something that fits the back cover copy (below). Surprise me!

When fleeing your past leads you straight to your future...
Delphine Harwick's seemingly perfect life in Rosmont Heights comes crashing down around her when her fiancé announces that he’s in love with her cousin. Heartbroken and reckless, she crashes her car on a winding coastal road—an accident that should have killed, or at least paralyzed her. Instead, she awakens mysteriously unharmed, rescued by what she initially believes to be an angel. Later, she finds out her hero is an enigmatic Irish paramedic named Tobin.
Stranded in the idyllic town of Fennel Cove, Delphine finds herself working at a charming inn and, for the first time, feeling like she belongs somewhere. The close-knit community embraces her, and she’s drawn to Tobin despite his obvious secrets. But Tobin is running from a dangerous past—his supernatural gift of healing nearly cost him everything when he couldn’t save a Chicago mob boss’s son.
As Delphine and Tobin grow closer, Tobin struggles to keep his abilities hidden. But when stories of miraculous healings in Fennel Cove begin surfacing on social media, his past catches up with him. When a Chicago reporter sent by a vengeful mob boss closes in, Tobin must choose between protecting his secret and finally facing up to his fears.
In a town where everyone knows everyone else's business, some secrets are too powerful to stay buried.
A heartwarming tale of second chances, supernatural gifts, and finding home in the most unexpected places.

Target Market(s)

women ages 20-70

Requirements
Must have
• illustrated, brightly colored, whimsical
Nice to have
• see description

```html
<!DOCTYPE html>
<html lang="en">
<head>
<meta charset="utf-8">
<title>Hollow Lanterns — Full Cover</title>
<link rel="stylesheet" href="https://fonts.googleapis.com/css2?family=Antonio:wght@600;700&family=Montserrat:wght@400&family=Cinzel:wght@500&display=swap">
<style>
  :root {
    --page: #ffffff;
    --violet: #4300a2;
    --violet-glow: #5418bd;
    --star: rgba(255,255,255,.55);
    --star-soft: rgba(190,160,255,.35);
    --gold: #d6a24a;
    --gold-light: #f3e2c4;
    --gold-deep: #b9771f;
    --copy: #ffffff;
    --sky: #b9e0f2;
    --mountain: #3f86b0;
    --lake: #3fb7b3;
    --forest: #0a1a22;
  }
  * { margin: 0; padding: 0; box-sizing: border-box; }
  html, body { width: 1200px; height: 844px; overflow: hidden; background: var(--page); }
  .cover-wrap {
    position: absolute; left: 22px; top: 22px; width: 1156px; height: 800px;
    background-color: var(--violet);
    background-image:
      radial-gradient(circle, var(--star) 0 0.8px, transparent 1.4px),
      radial-gradient(circle, var(--star) 0 0.6px, transparent 1.2px),
      radial-gradient(circle, var(--star-soft) 0 1.6px, transparent 3.5px),
      radial-gradient(circle, var(--star) 0 0.7px, transparent 1.3px),
      radial-gradient(circle, var(--star-soft) 0 2px, transparent 5px),
      radial-gradient(ellipse at 25% 20%, var(--violet-glow) 0%, transparent 45%),
      radial-gradient(ellipse at 80% 75%, var(--violet-glow) 0%, transparent 40%);
    background-size: 37px 29px, 53px 47px, 89px 71px, 23px 41px, 157px 131px, 100% 100%, 100% 100%;
    background-position: 5px 9px, 21px 3px, 40px 30px, 11px 17px, 70px 55px, 0 0, 0 0;
    overflow: hidden;
  }
  .starfield { position: absolute; left: 0; top: 0; }
  .back-title {
    position: absolute; left: 43px; width: 454px; top: 50px;
    font: 700 30px/1 "Antonio", sans-serif; color: var(--gold);
    text-align: center; letter-spacing: .3px;
  }
  .back-copy, .author-bio {
    position: absolute;
    font: 400 12.6px/18.8px "Montserrat", sans-serif; color: var(--copy);
  }
  .back-copy { left: 43px; top: 120px; width: 454px; }
  .author-bio { left: 194px; top: 480px; width: 303px; }
  .line { display: block; text-align: justify; text-align-last: justify; }
  .line.end { text-align-last: left; }
  .rule { position: absolute; left: 43px; width: 454px; height: 1px; background: var(--gold); }
  .rule.top { top: 446px; }
  .rule.bottom { top: 637px; }
  .author-photo {
    position: absolute; left: 50px; top: 465px; width: 126px; height: 154px;
    background: var(--page);
  }
  .spine, .front-type { position: absolute; left: 0; top: 0; }
  .illustration {
    position: absolute; left: 710px; top: 335px; width: 362px; height: 362px;
    border-radius: 50%;
    background: linear-gradient(180deg, var(--sky) 0%, #8cc6e2 18%, var(--mountain) 34%, #1d4f72 48%, #4fc6ee 56%, var(--lake) 68%, #1f5a4e 82%, var(--forest) 100%);
  }
</style>
</head>
<body>
<div class="cover-wrap">
  <svg width="0" height="0" style="position:absolute">
    <defs>
      <linearGradient id="goldFoil" x1="0" y1="0" x2="1" y2="1">
        <stop offset="0" stop-color="#f3e2c4"/>
        <stop offset="0.35" stop-color="#d6a24a"/>
        <stop offset="0.55" stop-color="#f3e2c4"/>
        <stop offset="0.8" stop-color="#b9771f"/>
        <stop offset="1" stop-color="#f3e2c4"/>
      </linearGradient>
      <path id="sparkle" d="M0 -9 L1.3 -1.3 L9 0 L1.3 1.3 L0 9 L-1.3 1.3 L-9 0 L-1.3 -1.3 Z" fill="rgba(255,255,255,.75)"/>
    </defs>
  </svg>

  <svg class="starfield" width="1156" height="800" aria-hidden="true">
    <g fill="rgba(255,255,255,.7)">
      <circle cx="210" cy="35" r="4" fill="rgba(200,170,255,.35)"/>
      <circle cx="132" cy="33" r="1.2"/><circle cx="388" cy="22" r="1.4"/><circle cx="612" cy="18" r="1.1"/>
      <circle cx="760" cy="70" r="1.3"/><circle cx="1115" cy="40" r="1.2"/><circle cx="1050" cy="210" r="1.4"/>
      <circle cx="640" cy="330" r="1.2"/><circle cx="510" cy="580" r="1.3"/><circle cx="540" cy="700" r="1.1"/>
      <circle cx="300" cy="710" r="4" fill="rgba(200,170,255,.35)"/><circle cx="125" cy="755" r="3" fill="rgba(200,170,255,.3)"/>
      <circle cx="1120" cy="600" r="3.5" fill="rgba(200,170,255,.3)"/><circle cx="660" cy="480" r="3" fill="rgba(200,170,255,.3)"/>
      <circle cx="30" cy="270" r="1.3"/><circle cx="20" cy="520" r="1.2"/><circle cx="1130" cy="370" r="1.3"/>
      <circle cx="1040" cy="720" r="1.2"/><circle cx="880" cy="790" r="1.1"/><circle cx="690" cy="760" r="1.3"/>
    </g>
    <use href="#sparkle" transform="translate(490 70)"/>
    <use href="#sparkle" transform="translate(680 440) scale(.8)"/>
    <use href="#sparkle" transform="translate(675 585) scale(1.1)"/>
    <use href="#sparkle" transform="translate(1040 150) scale(1.3)"/>
    <use href="#sparkle" transform="translate(498 655) scale(.7)"/>
    <use href="#sparkle" transform="translate(178 670) scale(.6)"/>
    <use href="#sparkle" transform="translate(930 165) scale(.7)"/>
  </svg>

  <h2 class="back-title">HOLLOW LANTERNS</h2>
  <p class="back-copy">
    <span class="line">Lorem ipsum dolor sit amet, consectetuer adipiscing elit, sed diam</span>
    <span class="line">nonummy nibh euismod tincidunt ut laoreet dolore magna aliquam</span>
    <span class="line">erat volutpat. Ut wisi enim ad minim veniam, quis nostrud exerci tation</span>
    <span class="line">ullamcorper suscipit lobortis nisl ut aliquip ex ea commodo consequat.</span>
    <span class="line">Duis autem vel eum iriure dolor in hendrerit in vulputate velit esse</span>
    <span class="line">molestie consequat, vel illum dolore eu feugiat nulla facilisis at vero</span>
    <span class="line">eros et accumsan et iusto odio dignissim qui blandit praesent luptatum</span>
    <span class="line end">zzril delenit augue duis dolore te feugait nulla facilisi.</span>
    <span class="line">Lorem ipsum dolor sit amet, cons ectetuer adipiscing elit, sed diam</span>
    <span class="line">nonummy nibh euismod tincidunt ut laoreet dolore magna aliquam</span>
    <span class="line">erat volutpat. Ut wisi enim ad minim veniam, quis nostrud exerci tation</span>
    <span class="line">ullamcorper suscipit lobortis nisl ut aliquip ex ea commodo consequat.</span>
    <span class="line">Lorem ipsum dolor sit amet, consectetuer adipiscing elit, sed diam</span>
    <span class="line">nonummy nibh euismod tincidunt ut laoreet dolore magna aliquam</span>
    <span class="line">erat volutpat. Ut wisi enim ad minim veniam, quis nostrud exerci tation</span>
    <span class="line">ullamcorper suscipit lobortis nisl ut aliquip ex ea commodo consequat.</span>
    <span class="line">Duis autem vel eum iriure dolor in hendrerit in vulputate velit esse</span>
  </p>

  <div class="rule top"></div>
  <div class="author-photo" role="img" aria-label="Author photo placeholder"></div>
  <p class="author-bio">
    <span class="line">Lorem ipsum dolor sit amet, consectetuer</span>
    <span class="line">adipiscing elit, sed diam nonummy nibh euis-</span>
    <span class="line">mod tincidunt ut laoreet dolore magna aliquam</span>
    <span class="line">erat volutpat. Ut wisi enim ad minim veniam,</span>
    <span class="line">quis nostrud exerci tation ullamcorper suscipit</span>
    <span class="line">lobortis nisl ut aliquip ex ea commodo conse-</span>
    <span class="line">quat. Duis autem vel eum iriure dolor in hen-</span>
    <span class="line">drerit in vulputate velit esse molestie conse-</span>
  </p>
  <div class="rule bottom"></div>

  <svg class="spine" width="1156" height="800" aria-label="Spine">
    <text transform="translate(570 54) rotate(90)" textLength="362" lengthAdjust="spacing"
          font-family="Antonio, sans-serif" font-weight="700" font-size="40" fill="url(#goldFoil)">HOLLOW LANTERNS</text>
    <text transform="translate(572 547) rotate(90)" textLength="209" lengthAdjust="spacing"
          font-family="Cinzel, serif" font-weight="500" font-size="38" fill="url(#goldFoil)">M.J. LOWE</text>
  </svg>

  <svg class="front-type" width="1156" height="800" aria-label="Front cover title and author">
    <text x="704" y="166" textLength="370" lengthAdjust="spacingAndGlyphs"
          font-family="Antonio, sans-serif" font-weight="700" font-size="158" fill="url(#goldFoil)">HOLLOW</text>
    <text x="676" y="303" textLength="427" lengthAdjust="spacingAndGlyphs"
          font-family="Antonio, sans-serif" font-weight="700" font-size="158" fill="url(#goldFoil)">LANTERNS</text>
    <text x="889" y="767" text-anchor="middle" textLength="232" lengthAdjust="spacingAndGlyphs"
          font-family="Cinzel, serif" font-weight="500" font-size="52" fill="url(#goldFoil)">M.J. LOWE</text>
  </svg>

  <div class="illustration" role="img" aria-label="Circular whimsical illustration: blue mountains and birds over a turquoise lake framed by pine trees, a man walking a golden dog and a woman in a grey hoodie"></div>
</div>
</body>
</html>
```